Referral Portal - Mobile App Design

To create a clean easy Web App Design for a Referral portal for Customer to submit and track their referrals.

Larkmoor Energy Referral Portal

https://www.larkmoor-energy.example

We are looking for a very simple phone app that will allow users to track their referrals. The sections/ things
We need in the app are as follows:
Form to Submit new Referrals
A very visual easy to read dashboard/ graph to show total Paid vs total potential(outstanding)
Simple Visual to show total paid
List of all referrals submitted and their status
Total number of referrals submitted and what Tier they fall into and what is the next tier (how close)

The App should be a minimal clean design that the user can navigate easily without much direction given.
This app should only be designed for the mobile experience. This is meant to gamify and incentives the user
To add more referrals and get more payments. Adding something fun with the Sun would be great!

Please See Bridge file for further information. We would like to name the App Larkmoor Energy Bridge

Thank you!!

Target Market(s)

Homeowners between ages of 30-60 who are familiar with apps that they use on their phone every day

Industry/Entity Type

Solar Energy

Font styles to use
Sans Serif

Colors
fbee3e
acd136
9bcb3c
f68e4e
f37022
f78f20
ffc214
34a7d8

Requirements
Must have
• Clean simple design, easy to use design/layout of nav.
• Visual charts and big graphic $$ on how much they have in their Wallet
• Easy visual to tell apart tiers (Gold, Silver,Platinum)
Nice to have
• Fun way to incorporate a rising or glowing sun
Should not have
• Too many words, not be bright and color

```html
<!DOCTYPE html>
<html lang="en">
<head>
<meta charset="utf-8">
<title>Referrals</title>
<link href="https://fonts.googleapis.com/css2?family=Roboto:wght@300;400;500;700&display=swap" rel="stylesheet">
<style>
  :root {
    --orange: #f9914e;
    --orange-deep: #e07f3e;
    --white: #ffffff;
    --ink: #222222;
    --muted: #7d7d7d;
    --pending: #808080;
    --approved: #9ccb2c;
  }
  * { box-sizing: border-box; margin: 0; padding: 0; }
  html, body {
    width: 676px; height: 1200px; overflow: hidden;
    background: var(--white);
    font-family: "Roboto", Arial, sans-serif;
  }
  .screen { position: relative; width: 676px; height: 1200px; overflow: hidden; background: var(--white); }

  .status-bar {
    position: absolute; left: 0; top: 0; width: 676px; height: 40px;
    background: var(--orange-deep); color: var(--white);
    font-size: 22px; font-weight: 400;
  }
  .status-bar .signal { position: absolute; left: 10px; top: 11px; }
  .status-bar .time { position: absolute; left: 0; right: 0; top: 7px; text-align: center; }
  .status-bar .battery-level { position: absolute; left: 553px; top: 8px; }
  .status-bar .battery { position: absolute; left: 615px; top: 10px; }

  .app-header {
    position: absolute; left: 0; top: 40px; width: 676px; height: 89px;
    background: var(--orange); color: var(--white);
  }
  .app-header .menu { position: absolute; left: 31px; top: 33px; }
  .app-header .title {
    position: absolute; left: 0; right: 0; top: 25px; text-align: center;
    font-size: 34px; font-weight: 300;
  }

  .tier {
    position: absolute; left: 0; right: 0; top: 132px; text-align: center;
    font-size: 72px; font-weight: 300; color: var(--orange); letter-spacing: 1px;
  }
  .referral-count-label {
    position: absolute; left: 122px; top: 241px;
    font-size: 33px; font-weight: 300; color: var(--orange);
  }
  .referral-count {
    position: absolute; left: 411px; top: 229px; width: 177px; height: 61px;
    border-radius: 31px; background: var(--orange); color: var(--white);
    font-size: 31px; font-weight: 300; line-height: 61px; text-align: center;
  }

  .column-heads { position: absolute; left: 0; top: 414px; width: 676px; height: 40px; font-size: 33px; font-weight: 500; color: var(--ink); }
  .column-heads span { position: absolute; top: 0; transform: translateX(-50%); }
  .col-name { left: 110px; top: 2px !important; }
  .col-date { left: 314px; }
  .col-state { left: 566px; }

  .referral {
    position: absolute; left: 26px; width: 624px; height: 61px;
    border: 2px solid var(--orange); border-radius: 31px;
  }
  .referral .name {
    position: absolute; left: 0; width: 190px; top: 0; line-height: 57px; text-align: center;
    font-size: 33px; font-weight: 300; color: var(--orange);
  }
  .referral .date {
    position: absolute; left: 188px; width: 200px; top: 0; line-height: 57px; text-align: center;
    font-size: 24px; font-weight: 300; color: var(--muted);
  }
  .referral .state {
    position: absolute; right: -2px; top: -2px; width: 175px; height: 61px; border-radius: 31px;
    color: var(--white); font-size: 24px; font-weight: 300; line-height: 61px; text-align: center;
  }
  .state.pending { background: var(--pending); }
  .state.approved { background: var(--approved); }

  .refer-button {
    position: absolute; left: 0; top: 1099px; width: 676px; height: 101px;
    background: var(--orange); color: var(--white);
    font-size: 33px; font-weight: 300; line-height: 101px; text-align: center; letter-spacing: 0.5px;
  }
</style>
</head>
<body>
<div class="screen">
  <div class="status-bar">
    <svg class="signal" width="116" height="18" viewBox="0 0 116 18" aria-hidden="true">
      <circle cx="8" cy="9" r="6.5" fill="#fff"/>
      <circle cx="24" cy="9" r="6.5" fill="#fff"/>
      <circle cx="40" cy="9" r="6.5" fill="#fff"/>
      <circle cx="56" cy="9" r="5.8" fill="none" stroke="#fff" stroke-width="1.4"/>
      <circle cx="72" cy="9" r="5.8" fill="none" stroke="#fff" stroke-width="1.4"/>
      <path d="M91 6 a14 14 0 0 1 20 0 M94 9.5 a9 9 0 0 1 14 0 M97.5 13 a4 4 0 0 1 7 0" fill="none" stroke="#fff" stroke-width="2.2" stroke-linecap="round"/>
      <circle cx="101" cy="16" r="1.6" fill="#fff"/>
    </svg>
    <span class="time">08:46 PM</span>
    <span class="battery-level">57%</span>
    <svg class="battery" width="52" height="22" viewBox="0 0 52 22" aria-hidden="true">
      <rect x="1" y="1" width="45" height="20" rx="4" fill="none" stroke="#fff" stroke-width="2"/>
      <rect x="4" y="4" width="25" height="14" rx="2" fill="#fff"/>
      <rect x="47.5" y="7" width="3" height="8" rx="1.5" fill="#fff"/>
    </svg>
  </div>

  <header class="app-header">
    <svg class="menu" width="44" height="26" viewBox="0 0 44 26" aria-label="Menu" role="img">
      <rect x="0" y="0" width="44" height="4" rx="2" fill="#fff"/>
      <rect x="0" y="11" width="44" height="4" rx="2" fill="#fff"/>
      <rect x="0" y="22" width="44" height="4" rx="2" fill="#fff"/>
    </svg>
    <h1 class="title">Referrals</h1>
  </header>

  <div class="tier">SILVER</div>
  <div class="referral-count-label">You Have Refered :</div>
  <div class="referral-count">3</div>

  <div class="column-heads">
    <span class="col-name">Names</span>
    <span class="col-date">Date</span>
    <span class="col-state">State</span>
  </div>

  <div class="referral" style="top:479px">
    <span class="name">Adam</span>
    <span class="date">2 Days Ago</span>
    <span class="state pending">PENDING</span>
  </div>
  <div class="referral" style="top:574px">
    <span class="name">Luis</span>
    <span class="date">5 Days Ago</span>
    <span class="state approved">APPROVED</span>
  </div>
  <div class="referral" style="top:680px">
    <span class="name">Sarah</span>
    <span class="date">2 Weeks Ago</span>
    <span class="state approved">APPROVED</span>
  </div>

  <div class="refer-button">REFER NEW FRIEND</div>
</div>
</body>
</html>
```